New Website for ReBranded Company - CrewBeacon

We have a successful company and website currently but it is a little dated. We have re-branded the company from Harbor Signal Networks to CrewBeacon and have a new logo for the new name. We are looking to build a newer fresher website with the new name. I will need a concept of the home page and one inside page. You can see our current site at https://www.harborsignalnetworks.example and the new site will be https://www.crewbeacon.example .

I also really like the https://www.pathlantern.example/ website. I like ledgerkite.example website. I like the https://skillorbit.example/ website.

See the attached document for layout and some text to use. Use the pictures I attached as opposed to pictures from the old site as much as you can.

Target Market(s)

Business

Industry/Entity Type

Software Service

Number of Pages Required

2 page

Font styles to use
Sans Serif

Requirements
Must have
• Use the colors from my logo. Professional but modern. We want people to feel like our product makes their staff feel safer at work.
Should not have
• Don't use any red or orange (no stop colors).

```html
<!DOCTYPE html>
<html lang="en">
<head>
<meta charset="utf-8">
<title>CrewBeacon – Electronic Panic Button</title>
<link href="https://fonts.googleapis.com/css2?family=Poppins:wght@400;500;600;700;800;900&display=swap" rel="stylesheet">
<style>
:root{
  --blue:#2f9be3;
  --blue-bright:#1a8cf0;
  --blue-dark:#1d7fc4;
  --navy:#174a8c;
  --green:#6cb33f;
  --ink:#2b2b2b;
  --grey:#555;
  --card:#f2f2f2;
  --white:#fff;
}
*{margin:0;padding:0;box-sizing:border-box}
html,body{width:1200px;height:3693px;overflow:hidden}
body{font-family:'Poppins',sans-serif;color:var(--ink);background:var(--white)}
.page{position:relative;width:1200px;height:3693px;overflow:hidden}
.abs{position:absolute}
.photo{position:absolute;left:0;width:1200px}
.btn{position:absolute;display:flex;align-items:center;justify-content:center;border-radius:30px;color:var(--white);font-weight:700;font-size:18px;letter-spacing:.2px;text-decoration:none}
.btn-blue{background:var(--blue)}
.btn-green{background:var(--green)}
.hl{color:var(--blue)}
.display{font-weight:900;text-transform:uppercase;letter-spacing:-.5px;color:var(--white);line-height:53px}

/* hero */
.hero{top:0;height:690px;background:linear-gradient(100deg,#2c3033 0%,#5d6468 40%,#3e4346 70%,#6e6f66 100%)}
.topbar{top:10px;left:720px;display:flex;gap:44px;color:var(--white);font-size:12px;font-weight:600;align-items:center}
.topbar span{display:flex;align-items:center;gap:8px}
.dot-icon{width:24px;height:24px;border-radius:50%;background:var(--blue);display:flex;align-items:center;justify-content:center}
.brand{display:flex;align-items:center;gap:10px;color:var(--blue);font-weight:600;font-size:32px}
.brand .mark{width:54px;height:54px;border-radius:50%;background:var(--blue)}
.nav{top:66px;left:482px;display:flex;align-items:center;font-size:12px;font-weight:600;color:var(--white)}
.nav a{color:var(--white);text-decoration:none}
.pill{display:flex;align-items:center;justify-content:center;border-radius:20px;height:38px;font-weight:700}
.hero-title{top:258px;left:150px;font-size:40px}
.hero-sub{top:384px;left:150px;color:var(--white);font-size:15px;font-weight:500}
.hero-sub b{color:var(--blue);font-weight:800}

.feature-card{top:611px;left:150px;width:900px;height:250px;background:var(--white);border-radius:14px 14px 0 0}
.feature{position:absolute;top:34px;width:300px;text-align:center;font-size:13.5px;font-weight:600;line-height:19px}
.feature svg{display:block;margin:0 auto 22px}

/* help band */
.help{top:903px;height:521px;background:linear-gradient(110deg,#5b6770 0%,#2e3640 45%,#1c2228 100%)}
.center{left:0;width:1200px;text-align:center}
.help-title{top:995px;font-size:38px}
.help-sub{top:1148px;color:var(--white);font-size:15px;line-height:26px;font-weight:500}

/* why */
.section-title{font-weight:800;font-size:37px;color:#444;letter-spacing:-.5px;text-transform:uppercase}
.why-col{position:absolute;top:1577px;width:330px;text-align:center}
.why-col h3{font-size:15px;font-weight:700;margin:26px 0 14px;text-transform:uppercase}
.why-col p{font-size:11px;line-height:18px;color:var(--grey)}
.options{display:grid;grid-template-columns:1fr 1fr;text-align:left;font-size:11px;line-height:18px;color:var(--grey);margin-top:8px}
.options .r{text-align:right}

/* earth */
.earth{top:1864px;height:549px;background:radial-gradient(ellipse at 50% 110%,#1d3d66 0%,#0c1a30 45%,#060b16 100%)}
.earth-title{top:1926px;font-size:38px}
.earth-sub{top:2048px;color:var(--white);font-size:15px;line-height:27px;font-weight:500}
.stats{top:2112px;left:0;width:1200px;display:flex;justify-content:center;align-items:center;color:var(--white)}
.badge{width:58px;height:58px;border-radius:50%;background:var(--white);color:var(--blue);font-weight:800;font-size:32px;display:flex;align-items:center;justify-content:center}
.stat{display:flex;align-items:center;gap:14px;font-weight:800;font-size:31px;text-transform:uppercase}
.covering{font-size:22px;font-weight:500;margin:0 48px}

/* plans */
.plan{position:absolute;top:2532px;width:277px;height:350px;background:var(--card)}
.plan-head{height:84px;color:var(--white);text-align:center;padding-top:10px}
.plan-head h4{font-size:28px;font-weight:800;line-height:34px}
.plan-head p{font-size:13px;font-weight:600;line-height:15px;margin-top:4px}
.plan ul{list-style:none;padding:18px 38px 0;font-size:15px;color:#444}
.plan li{padding:8px 0 8px;border-bottom:1px solid #d8d8d8}
.plan li:last-child{border:none}
.plan .note{padding:34px 10px 0;text-align:center;font-size:15px;line-height:22px;color:#444}
.plan .btn{left:33px;bottom:30px;width:210px;height:52px;font-size:19px}
.special-line{top:2931px;left:162px;width:876px;height:3px;background:var(--blue-dark)}
.special-title{top:2950px;left:196px;font-size:22px;font-weight:600}
.special-text{top:2983px;left:196px;font-size:12px;line-height:21px;color:#444}

/* cta */
.cta{top:3087px;height:225px;background:linear-gradient(100deg,#152640 0%,#1e3e6e 50%,#1a3458 80%,#243a5c 100%)}
.cta-title{top:3146px;left:150px;font-size:38px}

/* footer */
.footer{top:3312px;height:381px;background:linear-gradient(120deg,#0d3c78 0%,#1762ad 45%,#0f4d93 100%)}
.foot-about{top:3418px;left:150px;width:230px;color:var(--white);font-size:12px;line-height:20px}
.foot-col{position:absolute;top:3340px;color:var(--white)}
.foot-col h5{font-size:17px;font-weight:700;text-transform:uppercase}
.foot-col h5:after{content:"";display:block;width:30px;height:3px;background:var(--green);margin-top:6px;margin-bottom:10px}
.foot-col a{display:block;color:var(--white);text-decoration:none;font-size:13px;line-height:32px;font-weight:500}
.call{top:3535px;left:150px;display:flex;align-items:center;gap:16px;color:var(--white)}
.call .t1{font-size:18px;font-weight:700;text-align:center}
.call .t2{font-size:20px;font-weight:800}
.foot-line{top:3627px;left:150px;width:900px;height:1px;background:rgba(255,255,255,.3)}
.copyright{top:3650px;left:0;width:1200px;text-align:center;color:var(--white);font-size:9px}
</style>
</head>
<body>
<div class="page">

  <!-- Hero -->
  <div class="photo hero" role="img" aria-label="Hand pressing a panic button mounted under a desk"></div>
  <div class="abs topbar">
    <span><span class="dot-icon"><svg width="10" height="10" viewBox="0 0 10 10"><path d="M2 1l7 4-7 4z" fill="#fff"/></svg></span>SCHEDULE A DEMO</span>
    <span><span class="dot-icon"><svg width="12" height="12" viewBox="0 0 24 24"><path d="M6.6 10.8a15 15 0 0 0 6.6 6.6l2.2-2.2a1 1 0 0 1 1-.25 11.4 11.4 0 0 0 3.6.57 1 1 0 0 1 1 1V20a1 1 0 0 1-1 1A17 17 0 0 1 3 4a1 1 0 0 1 1-1h3.5a1 1 0 0 1 1 1 11.4 11.4 0 0 0 .57 3.6 1 1 0 0 1-.25 1z" fill="#fff"/></svg></span>1 – 800 – 555 – 0142</span>
  </div>
  <div class="abs brand" style="top:52px;left:150px"><span class="mark"></span>CrewBeacon</div>
  <nav class="abs nav">
    <a href="#" style="margin-right:82px">HOME</a>
    <a href="#" style="margin-right:40px">BUY ADDONS</a>
    <a href="#" class="pill" style="background:var(--green);width:88px;margin-right:40px">LOGIN</a>
    <a href="#" class="pill" style="background:var(--blue);width:208px">EXPLORE YOUR CHOICES</a>
  </nav>
  <h1 class="abs display hero-title">Feel confident that<br>your staff is <span class="hl">protected</span></h1>
  <p class="abs hero-sub">GET A REVOLUTIONARY NEW ELECTRONIC <b>PANIC BUTTON</b></p>
  <a href="#" class="btn btn-blue" style="top:437px;left:150px;width:208px;height:52px">GET STARTED</a>

  <div class="abs feature-card">
    <div class="feature" style="left:0">
      <svg width="76" height="76" viewBox="0 0 72 72" fill="none" stroke="#2f9be3" stroke-width="2.4" stroke-linecap="round"><path d="M36 14a12 12 0 0 0-7 22v6h14v-6a12 12 0 0 0-7-22z"/><path d="M30 46h12M32 4v4M14 22h4M54 22h4M20 8l3 3M52 8l-3 3"/><path d="M6 56l12-6h14l8 4-10 2h-6M18 64l14 4 26-12-4-4-14 4"/></svg>
      Problems Stopped Before They Start<br>For Any Type Of Organization
    </div>
    <div class="feature" style="left:300px">
      <svg width="80" height="76" viewBox="0 0 80 72" fill="none" stroke="#2f9be3" stroke-width="2.4" stroke-linecap="round" stroke-linejoin="round"><path d="M46 22c-4-4-14-3-14 3s14 4 14 11-10 8-15 3M39 14v34"/><path d="M50 18l10-12 14 6-10 12zM4 56l10-12 14 6-10 12z"/><path d="M22 36h8M50 36h8"/></svg>
      Affordable Prices Starting at $18 per month.<br>No Contracts. No Hidden Costs.
    </div>
    <div class="feature" style="left:600px">
      <svg width="80" height="76" viewBox="0 0 80 72" fill="none" stroke="#2f9be3" stroke-width="3" stroke-linejoin="round"><path d="M40 4L76 66H4z"/><path d="M40 26v20M40 53v4" stroke-linecap="round"/></svg>
      Alerts by computer, mobile device,<br>text, phone, email, monitoring and E911
    </div>
  </div>

  <!-- Help band -->
  <div class="photo help" role="img" aria-label="Desk phone beside a two-button alert unit on an office desk"></div>
  <h2 class="abs center display help-title">Your empoyees shouldn’t<br>feel alone when they need <span class="hl">help</span></h2>
  <p class="abs center help-sub">DOES THIS PROBLEM MAKE YOU FEEL FRUSTRATED AND ANXIOUS?<br>PUT A SIMPLE SOLUTION IN THEIR HANDS</p>
  <a href="#" class="btn btn-blue" style="top:1262px;left:495px;width:209px;height:50px">LEARN MORE</a>

  <!-- Why choose us -->
  <h2 class="abs center section-title" style="top:1486px">Why choose us</h2>
  <div class="why-col" style="left:100px">
    <svg width="60" height="80" viewBox="0 0 60 80" fill="none" stroke="#2f9be3" stroke-width="2.4" stroke-linecap="round" stroke-linejoin="round"><path d="M22 42V14a5 5 0 0 1 10 0v22l14 3c5 1 7 5 6 10l-3 16c-1 4-4 7-8 7H30c-3 0-6-2-8-5L10 52c-2-3 0-7 4-7 3 0 5 2 8 5"/><path d="M14 16a13 13 0 0 1 26 0M18 16a9 9 0 0 1 18 0"/></svg>
    <h3>Easy to use</h3>
    <p>Press a button and let the right people know<br>you need help and open a chat window<br>letting everyone talk on resolving their<br>problem.</p>
  </div>
  <div class="why-col" style="left:435px">
    <svg width="80" height="80" viewBox="0 0 80 80" fill="none" stroke="#2f9be3" stroke-width="2.4" stroke-linejoin="round"><rect x="4" y="4" width="16" height="26"/><rect x="54" y="4" width="22" height="14"/><path d="M28 48a8 8 0 0 1 4-14 10 10 0 0 1 18 2 7 7 0 0 1 0 12z"/><rect x="4" y="56" width="22" height="20"/><rect x="58" y="52" width="16" height="24"/><path d="M12 30v26M65 18v16M26 66h14V48M58 62H48V48M50 36h15"/></svg>
    <h3>Communicate the way you want</h3>
    <p>We give you lots of options:</p>
    <div class="options"><span>Computer</span><span class="r">Text</span><span>Mobile</span><span class="r">E911</span><span>Email</span><span class="r">Call Center</span><span>Phone call</span></div>
  </div>
  <div class="why-col" style="left:771px">
    <svg width="64" height="80" viewBox="0 0 64 80" fill="none" stroke="#2f9be3" stroke-width="2.6" stroke-linejoin="round" stroke-linecap="round"><path d="M32 4L60 14v22c0 20-12 32-28 40C16 68 4 56 4 36V14z"/><path d="M20 40l9 9 16-17"/></svg>
    <h3>Cost effective protection</h3>
    <p>By leveraging your existing network and<br>equipment we can lower your costs to give<br>better options to your staff.</p>
  </div>

  <!-- Coverage -->
  <div class="photo earth" role="img" aria-label="Earth from orbit at night with city lights"></div>
  <h2 class="abs center display earth-title">We know how scary it can feel to<br>worry about employee <span class="hl">safety</span></h2>
  <p class="abs center earth-sub">THAT'S WHY WE HAVE PROVIDED A WAY FOR<br>CUSTOMERS TO GET HELP TO STAFF EFFECTIVELY IN</p>
  <div class="abs stats">
    <div class="stat"><span class="badge">45</span>States</div>
    <span class="covering">COVERING</span>
    <div class="stat"><span class="badge">5</span>Countries</div>
  </div>
  <svg class="abs" style="top:2188px;left:565px" width="70" height="70" viewBox="0 0 70 70" fill="none" stroke="#2f9be3" stroke-width="2.5"><circle cx="35" cy="35" r="32"/><path d="M28 22l18 13-18 13z" stroke-linejoin="round"/></svg>
  <a href="#" class="btn btn-blue" style="top:2294px;left:495px;width:210px;height:52px">WATCH MY DEMO</a>

  <!-- Plans -->
  <h2 class="abs center section-title" style="top:2454px">Simple start <span class="hl">plan</span></h2>
  <div class="plan" style="left:150px">
    <div class="plan-head" style="background:var(--green)"><h4>STEP 01</h4><p>EXPLORE YOUR CHOICES</p></div>
    <ul><li>• Pricing</li><li>• Trial</li><li>• Quote</li><li>• Hardware</li></ul>
    <a href="#" class="btn btn-blue">GET STARTED</a>
  </div>
  <div class="plan" style="left:456px">
    <div class="plan-head" style="background:var(--blue-bright)"><h4>STEP 02</h4><p>GET SETUP</p></div>
    <ul><li>• Input Your Alerts</li><li>• Input Your Staff</li><li>• Install Our Software</li></ul>
    <a href="#" class="btn btn-blue">INSTALL</a>
  </div>
  <div class="plan" style="left:773px">
    <div class="plan-head" style="background:var(--navy)"><h4>STEP 03</h4><p>FEEL CONFIDENT YOUR STAFF IS<br>PROTECTED</p></div>
    <p class="note">High Five. You just too a major step to getting rid of the anxiety and frustration this gave you.</p>
    <a href="#" class="btn btn-blue">START MY DEMO</a>
  </div>
  <div class="abs special-line"></div>
  <h3 class="abs special-title">Need something else? Contact us for a special plan.</h3>
  <p class="abs special-text">Do you need a VPN, a dedicated server or maybe cloud hosting? No matter what it is, we have it!<br>Give us your technical details and we'll match them effortlessly and in no time at all.</p>
  <a href="#" class="btn btn-green" style="top:2954px;left:809px;width:208px;height:50px">GET QUOTE</a>

  <!-- CTA -->
  <div class="photo cta" role="img" aria-label="Emergency vehicle lights at night in blue tones"></div>
  <h2 class="abs display cta-title">Stay connected with staff during<br><span class="hl">a crisis situations</span></h2>
  <a href="#" class="btn btn-blue" style="top:3229px;left:812px;width:205px;height:50px">START MY DEMO</a>

  <!-- Footer -->
  <div class="photo footer" role="img" aria-label="Blue technology control panel background"></div>
  <div class="abs brand" style="top:3344px;left:150px;color:var(--white)"><span class="mark" style="background:var(--green)"></span>CrewBeacon</div>
  <p class="abs foot-about">When employees feel alone during a threatening situation, we give them a way to let the right resources know that they need help so you can feel confident that your staff is protected.</p>
  <div class="abs call">
    <svg width="50" height="50" viewBox="0 0 24 24" fill="none" stroke="#fff" stroke-width="1.2"><path d="M6.6 10.8a15 15 0 0 0 6.6 6.6l2.2-2.2a1 1 0 0 1 1-.25 11.4 11.4 0 0 0 3.6.57 1 1 0 0 1 1 1V20a1 1 0 0 1-1 1A17 17 0 0 1 3 4a1 1 0 0 1 1-1h3.5a1 1 0 0 1 1 1 11.4 11.4 0 0 0 .57 3.6 1 1 0 0 1-.25 1z"/><path d="M15 3a6 6 0 0 1 6 6M15 6a3 3 0 0 1 3 3"/></svg>
    <div><div class="t1">CALL US</div><div class="t2">1 – 800 – 555 – 0142</div></div>
  </div>
  <div class="foot-col" style="left:516px"><h5>Shop</h5><a href="#">ADD ONS</a><a href="#">START MY DEMO</a><a href="#">CUSTOM QUOTE</a><a href="#">START TRIAL</a></div>
  <div class="foot-col" style="left:708px"><h5>About</h5><a href="#">AFFILIATES</a><a href="#">CONTACT</a><a href="#">SUPPORT</a><a href="#">EXISTING CUSTOMERS</a><a href="#">INDUSTRIES</a><a href="#">BLOG</a><a href="#">FAQ</a></div>
  <div class="foot-col" style="left:932px"><h5>Legal</h5><a href="#">PRIVACY POLICY</a><a href="#">TERMS OF USE</a><a href="#">END USER LICENSE</a><a href="#">AGREEMENT</a></div>
  <div class="abs foot-line"></div>
  <p class="abs copyright">©CrewBeacon 2020. ALL RIGHTS RESERVED.</p>
</div>
</body>
</html>
```